Massage Therapy and Personal Training Business Card (RT Restful)

I need a logo design based in Washington. The company is called RT Restful. RT are my initials. I specialize in massage therapy and personal training and general wellness of my clients. I've tried getting designs but haven't quite yet found what I'm looking for. I'm not inclined to a certain color yet but some color that resembles wellness such as light blue and white or green and white. Again, I'm not really picky about that. Thank you in advance

Industry/Entity Type

Business

Contact Information for Business Card

Have the description on one side and space for writing information on the back side such as number, appt, etc. I have an example attached. I see a lot of these card. I dont want the exact one, but something similar. Simple, professional and elegant.

Colors

Designer to choose colors to be used in the design.

Requirements
Must have
• Space on the back side to write
• A professional, elegant look
Should not have
• cartoon like style.

```html
<!DOCTYPE html>
<html lang="en">
<head>
<meta charset="utf-8">
<title>RT Restful – Business Card</title>
<link href="https://fonts.googleapis.com/css2?family=Marcellus&family=Open+Sans:wght@400;600;700&display=swap" rel="stylesheet">
<style>
  :root {
    --green: #5a9a3c;
    --green-dark: #4e8a32;
    --ink: #3a3a3a;
    --card: #ffffff;
    --backdrop: #e9ebe6;
    --figure-light: #f2f2f2;
    --figure-mid: #d6d6d6;
  }
  html, body {
    margin: 0;
    width: 1200px;
    height: 1000px;
    overflow: hidden;
    background: var(--backdrop);
    font-family: "Open Sans", Arial, sans-serif;
  }
  .card {
    position: absolute;
    left: 266px;
    width: 666px;
    height: 397px;
    border-radius: 22px;
    background: var(--card);
    overflow: hidden;
    box-shadow: 0 4px 14px rgba(0,0,0,0.18);
  }
  .card-front { top: 74px; }
  .card-back { top: 533px; }
  .card svg.shapes { position: absolute; inset: 0; }
  .anatomy-art {
    position: absolute;
    left: 334px;
    top: 0;
    width: 310px;
    height: 372px;
    background: radial-gradient(ellipse at 50% 45%, var(--figure-mid) 0%, var(--figure-light) 60%, var(--card) 100%);
  }
  .text { position: absolute; left: 0; width: 348px; text-align: center; margin: 0; }
  .brand-name {
    top: 148px; font-family: "Marcellus", Georgia, serif;
    font-size: 39px; color: var(--green); letter-spacing: 0.5px;
  }
  .brand-mark {
    position: absolute; left: 150px; top: 54px; width: 58px; height: 58px;
    border-radius: 50%; background: var(--green); opacity: 0.9;
  }
  .brand-tagline { top: 185px; font-size: 20px; color: var(--ink); }
  .person-name { top: 234px; font-size: 18px; color: var(--green); }
  .person-title { top: 257px; font-size: 16px; color: var(--ink); }
  .phone { top: 287px; font-size: 16px; color: var(--ink); }
  .email { top: 310px; font-size: 16px; color: var(--ink); }

  .back-heading {
    position: absolute; top: 26px; left: 0; width: 100%; margin: 0; text-align: center;
    color: #fff; font-size: 17px; font-weight: 600; word-spacing: 3px;
  }
  .write-line { position: absolute; left: 137px; width: 393px; height: 0; border-top: 1.5px solid var(--ink); }
  .write-line.name-line { top: 139px; }
  .write-line.date-line { top: 264px; }
  .field-label {
    position: absolute; margin: 0; color: var(--green); font-size: 15px; font-weight: 600;
    transform: translateX(-50%);
  }
  .days {
    position: absolute; top: 190px; left: 33px; right: 33px;
    display: flex; justify-content: space-between; align-items: center;
  }
  .day { display: flex; align-items: center; gap: 13px; color: var(--green); font-weight: 600; font-size: 16px; }
  .day-box { width: 24px; height: 17px; border: 1.5px solid var(--ink); border-radius: 5px; }
  .policy { position: absolute; left: 0; width: 100%; text-align: center; margin: 0; color: var(--ink); font-size: 16px; }
  .policy-title { top: 324px; }
  .policy-text { top: 348px; }
</style>
</head>
<body>

<section class="card card-front">
  <div class="anatomy-art" role="img" aria-label="Anatomical illustration of a back and shoulders with highlighted muscle areas"></div>
  <svg class="shapes" width="666" height="397" viewBox="0 0 666 397">
    <path d="M0 348 Q330 395 666 346 L666 397 L0 397 Z" fill="var(--green)"/>
  </svg>
  <span class="brand-mark"></span>
  <p class="text brand-name">RT RESTFUL</p>
  <p class="text brand-tagline">Message Therapy</p>
  <p class="text person-name">DANIEL MORROW</p>
  <p class="text person-title">Massage Therapist</p>
  <p class="text phone">0438215067</p>
  <p class="text email">daniel@rtrestful.com</p>
</section>

<section class="card card-back">
  <svg class="shapes" width="666" height="397" viewBox="0 0 666 397">
    <path d="M0 0 L666 0 L666 56 Q330 50 0 79 Z" fill="var(--green)"/>
  </svg>
  <h2 class="back-heading">YOUR NEXT APPOINTMENT</h2>
  <div class="write-line name-line"></div>
  <p class="field-label" style="top:147px; left:333px;">NAME</p>
  <div class="days">
    <div class="day">Mon <span class="day-box"></span></div>
    <div class="day">Tue <span class="day-box"></span></div>
    <div class="day">Wed <span class="day-box"></span></div>
    <div class="day">Thur <span class="day-box"></span></div>
    <div class="day">Fri <span class="day-box"></span></div>
    <div class="day">Sat <span class="day-box"></span></div>
  </div>
  <div class="write-line date-line"></div>
  <p class="field-label" style="top:272px; left:242px;">DATE</p>
  <p class="field-label" style="top:272px; left:425px;">TIME</p>
  <p class="policy policy-title">CANCELATION POLICY</p>
  <p class="policy policy-text">If you are unable to keep your appointment , please allow 24 hours notice</p>
</section>

</body>
</html>
```